Book cover for book about ex-wifes

I need a book cover for my new book called "Naboer fra Bakken, Mosen og Tjørnelunde" - In english: "Neighbours from Hilltop, Marsh and Tjørnelunde" (Hørsholm is a posh city in Denmark).

The book is by men for men about ex-wifes and about how to avoid getting them.
Is it a book from a sexologist and couples therapist to men on how to improve relations.

Target Market(s)

Men (and curious women)

Requirements
Must have
• Something that indicate three types of ex-wifes

And the author name “Jonas Birkvig”
Nice to have
• Something that says something about relationships, couples and how to stay together (or how to avoid not breaking up)
Should not have
• No hate

```html
<!DOCTYPE html>
<html lang="da">
<head>
<meta charset="utf-8">
<title>Naboer fra Bakken, Mosen og Tjørnelunde – Jonas Birkvig</title>
<link href="https://fonts.googleapis.com/css2?family=Josefin+Sans:wght@600&family=Oswald:wght@600&display=swap" rel="stylesheet">
<style>
  :root {
    --concrete-light: #dcdcdc;
    --concrete-mid: #cbcbcb;
    --concrete-dark: #b9b9b9;
    --ink: #2d2d2d;
    --accent-red: #e8141f;
    --photo-light: #c9c2bb;
    --photo-dark: #6e655d;
  }
  html, body {
    margin: 0;
    padding: 0;
    width: 802px;
    height: 1200px;
    overflow: hidden;
    background: var(--concrete-mid);
  }
  .book-cover {
    position: relative;
    width: 802px;
    height: 1200px;
    overflow: hidden;
    background:
      radial-gradient(ellipse at 40% 35%, var(--concrete-light) 0%, var(--concrete-mid) 60%, var(--concrete-dark) 100%);
  }
  .cover-type {
    position: absolute;
    inset: 0;
    width: 802px;
    height: 1200px;
  }
  .author-name {
    font-family: "Josefin Sans", sans-serif;
    font-weight: 600;
    font-size: 54px;
    fill: var(--ink);
  }
  .title-line {
    font-family: "Oswald", sans-serif;
    font-weight: 600;
    fill: var(--ink);
  }
  .title-line .accent,
  .title-line.accent {
    fill: var(--accent-red);
  }
  .cover-photo {
    position: absolute;
    left: 30px;
    top: 800px;
    width: 742px;
    height: 400px;
    background:
      radial-gradient(ellipse at 25% 40%, var(--photo-light) 0%, transparent 55%),
      radial-gradient(ellipse at 72% 40%, var(--photo-dark) 0%, transparent 60%),
      linear-gradient(180deg, rgba(200,200,200,0) 0%, var(--photo-light) 45%, var(--photo-dark) 100%);
  }
</style>
</head>
<body>
  <main class="book-cover">
    <svg class="cover-type" viewBox="0 0 802 1200" xmlns="http://www.w3.org/2000/svg">
      <text class="author-name" x="190" y="104" textLength="416" lengthAdjust="spacingAndGlyphs">JONAS BIRKVIG</text>
      <text class="title-line" x="108" y="328" font-size="164" textLength="584" lengthAdjust="spacingAndGlyphs">NABOER</text>
      <text class="title-line" x="108" y="444" font-size="108" textLength="584" lengthAdjust="spacingAndGlyphs">FRA <tspan class="accent">BAKKEN</tspan></text>
      <text class="title-line accent" x="108" y="608" font-size="174" textLength="584" lengthAdjust="spacingAndGlyphs">MOSEN</text>
      <text class="title-line" x="108" y="752" font-size="123" textLength="584" lengthAdjust="spacingAndGlyphs">OG TJØRNELUNDE</text>
    </svg>
    <div class="cover-photo" role="img" aria-label="Photo of a woman in a white top looking away and a bearded man in a flat cap and waistcoat with crossed arms, standing side by side"></div>
  </main>
</body>
</html>
```